Tidewell Marketing company is looking for a web page design

Your projects should contain:

1. Header: Logo provided by us.
2. Top nav bar: offer, about us, experience, contact.
3. “Choose language” button.
4. Main section: panoramic picture (static, professional, modern).
5. Below section: 3 blocks (image+title+description), which represent our 3 main activities (titles):
• Market Research,
• Marketing Plans,
• Marketing Project.
6. ‘Contact us’ form – Message (text: “Write your message and give us details about your company and activities”), Email, SEND).
7. Page footer: (4 section: Contact, Social Media, Blog, Partners).
Updates

Hello!

I uploaded new file 'general_look', which is our idea how the page should generally look like.

BUT! it doesn't mean that your projects should look exactly like this project e.g.:
* titles Market Research, Marketing Plans, Marketing Project can be above these: Image 1,2,3.
* everything doesn't have to be in square and rectangle shape. You can try to manipulate with blocks and can add elipse elemnts or something similar.

We will appreciate your innovative ideas. Just wanted to give you general plan of the site and ilustrate all elements that we require.

Best Regards,
Benedek

IMPORTENT

Please remember that the main picture should be panoramic. Please do not close it in frame.

Target Market(s)

Small and middle sized companies, which would like to export their goods and services abroad and are interested in raising funds from Northgate Trade Council to expand their activities. These are rather industrial companies with low level of innovativeness. Our mission is to build image of the client’s company and increase awareness of their products to improve their competitiveness and innovativeness.

Industry/Entity Type

It Company

Requirements
Must have
• 1. Create designs of main page and subpage.
2. Subpage: Logo, Header, language button, place for article, navigation menu on the right side - below it “contact us” button , footer on the bottom. (In this section we are looking mainly for the design of the header and navigation menu).
3. The whole design should be a series of horizontal blocks.
4. Your projects should be associated with features such as: Reliability, Security, Professionalism, Openness, Uniqueness.
5. The design should be simple, fresh, readable, easy to use and should create a feeling of high quality services.
6. Possibility to change the panoramic picture (separate layer in a graphic file).
7. All pictures and blocks should be static, no movements.
8. Style of the page should be compliant with the logo design, font: Swiss.
9. Designs that we like: http://www.fernvale-studio.pl/, http://www.plumquarry.com/.
Should not have
• There shouldn’t be any distractions and not matching parts (whole design should be compact and easy to interpret and remember).

```html
<!DOCTYPE html>
<html lang="en">
<head>
<meta charset="utf-8">
<title>Tidewell Marketing</title>
<link href="https://fonts.googleapis.com/css2?family=Arimo:wght@400;700&family=Playfair+Display+SC:wght@700&display=swap" rel="stylesheet">
<style>
:root{
  --page:#a9a9a9;
  --sheet:#f2f2f2;
  --brand:#1b4f86;
  --ink:#222;
  --navy:#1c3d5c;
  --btn-top:#2d6a8e;
  --btn-bottom:#123a55;
  --band:#8c8c8c;
  --footer:#474747;
  --accent:#e8501a;
  --red:#a8281a;
}
*{box-sizing:border-box;margin:0;padding:0}
html,body{width:1058px;height:1200px;overflow:hidden}
body{background:var(--page);font-family:"Arimo",Arial,sans-serif;color:var(--ink);position:relative}
.sheet{position:absolute;left:49px;top:0;width:962px;height:1200px;
  background:linear-gradient(#dcdcdc 0,#ececec 130px,#fafafa 480px,#fafafa 842px)}
.logo{position:absolute;left:18px;top:30px;display:flex;align-items:center;gap:10px}
.logo-mark{width:56px;height:56px;border-radius:50%;background:var(--brand)}
.logo-name{font-size:36px;font-weight:700;color:var(--brand);letter-spacing:-1px}
.lang{position:absolute;left:754px;top:23px;width:175px;height:30px;border:1px solid #bdbdbd;border-radius:3px;
  background:linear-gradient(#fff,#ececec);font-size:14px;color:#888;padding:7px 8px;overflow:hidden}
.lang-arrow{position:absolute;right:0;top:0;width:24px;height:28px;background:linear-gradient(#3f9be6,#1a6fc4);
  display:flex;align-items:center;justify-content:center}
.nav{position:absolute;left:422px;top:69px;width:508px;height:47px;border:1px solid #c6c6c6;border-radius:4px;
  background:linear-gradient(#fbfbfb,#dedede);display:flex;overflow:hidden}
.nav a{flex:auto;text-align:center;padding-top:17px;font-size:17px;color:#333;text-decoration:none;border-left:1px solid #c9c9c9}
.nav a:first-child{border-left:0}
.hero{position:absolute;left:39px;top:145px;width:887px;height:315px;border-radius:6px;
  background:radial-gradient(circle at 52% 50%,#5cc8ff 0,#1a6fb0 14%,#24476a 30%,#aab6c4 60%,#c9d2dc 80%,#b46060 100%)}
.dots{position:absolute;left:26px;bottom:5px;display:flex;gap:8px}
.dots span{width:13px;height:13px;border-radius:50%;background:#bfc4c9}
.cards{position:absolute;left:39px;top:488px;display:flex;gap:17px}
.card{width:284px;height:334px;background:linear-gradient(#fff 230px,#ececec);border-radius:0 0 5px 5px;
  box-shadow:0 1px 3px rgba(0,0,0,.3);position:relative}
.card-img{height:122px}
.card-title{height:50px;font-size:20px;font-weight:700;color:var(--navy);padding:13px 19px;border-bottom:2px solid rgba(0,0,0,.15)}
.research .card-img{background:linear-gradient(#fff,#cfd8e4)}
.research .card-title{background:linear-gradient(#ffd73d,#f7b21b)}
.plans .card-img{background:linear-gradient(#4a8fd0,#c8dcef)}
.plans .card-title{background:linear-gradient(#b0e552,#78c42a)}
.projects .card-img{background:linear-gradient(#1e64b4,#8fc3ea)}
.projects .card-title{background:linear-gradient(#40c0f2,#1a8ed6)}
.card p{font-size:11.5px;line-height:23px;padding:16px 12px 0 13px;color:#333}
.more{position:absolute;left:95px;top:303px;width:94px;height:31px;border-radius:2px;
  background:linear-gradient(var(--btn-top),var(--btn-bottom));color:#fff;font-size:15px;text-align:center;padding-top:7px}
.contact{position:absolute;left:0;top:842px;width:962px;height:180px;background:var(--band)}
.contact-title{position:absolute;left:56px;top:17px;font-family:"Playfair Display SC",Georgia,serif;font-size:19px;color:var(--red)}
.contact-rule{position:absolute;left:39px;top:43px;width:884px;height:1px;background:#b5b5b5}
.panel{position:absolute;top:57px;height:101px;border-radius:5px;background:linear-gradient(#fafafa,#e3e3e3);border:1px solid #c3c3c3}
.panel-message{left:39px;width:433px}
.panel-message h3{font-size:17px;color:var(--navy);text-align:center;padding:5px 0 3px;border-bottom:1px solid #ccc}
.panel-message p{font-size:15.5px;line-height:20px;padding:10px 34px;color:#111}
.panel-form{left:491px;width:433px}
.field{position:absolute;left:89px;top:12px;width:263px;height:30px;border:1px solid #bbb;background:#fafafa;
  font-size:14px;color:#999;text-align:center;padding-top:7px}
.send{position:absolute;left:90px;top:55px;width:263px;height:33px;border-radius:3px;
  background:linear-gradient(#3a9fd5,#125a8a);color:#fff;font-size:16px;text-align:center;padding-top:8px;box-shadow:0 1px 2px rgba(0,0,0,.4)}
.footer{position:absolute;left:0;top:1022px;width:962px;height:178px;background:var(--footer)}
.col{position:absolute;top:25px;width:230px}
.col h4{font-weight:400;font-size:17px;color:var(--accent);padding-left:19px;position:relative}
.col h4::before{content:"";position:absolute;left:0;top:3px;border-left:8px solid var(--accent);border-top:6px solid transparent;border-bottom:6px solid transparent}
.col ul{list-style:none;margin-top:22px}
.col li{font-size:14.5px;line-height:18.5px;color:#fff;padding-left:19px;position:relative}
.col li::before{content:"";position:absolute;left:3px;top:8px;width:5px;height:5px;border-radius:50%;background:var(--accent)}
.divider{position:absolute;top:30px;height:128px;border-left:1px dotted #999}
</style>
</head>
<body>
<div class="sheet">
  <div class="logo"><span class="logo-mark"></span><span class="logo-name">tidewell marketing</span></div>
  <div class="lang">choose language<span class="lang-arrow"><svg width="12" height="8" viewBox="0 0 12 8"><path d="M0 0h12L6 8z" fill="#fff"/></svg></span></div>
  <nav class="nav"><a>Home</a><a>About Us</a><a>Experience</a><a>Contact Us</a></nav>

  <div class="hero" role="img" aria-label="Businessman in a suit holding a glowing blue globe in his open hand">
    <div class="dots"><span></span><span></span><span></span></div>
  </div>

  <div class="cards">
    <div class="card research">
      <div class="card-img" role="img" aria-label="Business team standing before large lettering with a rising orange arrow"></div>
      <div class="card-title">Market Research</div>
      <p>Nulla ut elit nunc, sed porka justo. Etlima none fasil impuma. Etrika egit isomiu posture postegeus nuho fedsfogij oijretoih er reog dfkngdg fdgklngdvgjnerelj sed velit. Mobile frideem technique predict...</p>
      <div class="more">More</div>
    </div>
    <div class="card plans">
      <div class="card-img" role="img" aria-label="Green street signs reading marketing and strategy against blue sky"></div>
      <div class="card-title">Marketing Plans</div>
      <p>Nulla ut elit nunc, sed porka justo. Etlima none fasil impuma. Etrika egit isomiu posture postegeus nuho fedsfogij oijretoih er reog dfkngdg fdgklngdvgjnerelj sed velit. Mobile frideem technique predict...</p>
      <div class="more">More</div>
    </div>
    <div class="card projects">
      <div class="card-img" role="img" aria-label="Man looking up at a green success sign under a blue sky"></div>
      <div class="card-title">Marketing Projects</div>
      <p>Nulla ut elit nunc, sed porka justo. Etlima none fasil impuma. Etrika egit isomiu posture postegeus nuho fedsfogij oijretoih er reog dfkngdg fdgklngdvgjnerelj sed velit. Mobile frideem technique predict...</p>
      <div class="more">More</div>
    </div>
  </div>

  <section class="contact">
    <div class="contact-title">Contact Us</div>
    <div class="contact-rule"></div>
    <div class="panel panel-message">
      <h3>Message</h3>
      <p>Write your message and give us details about your company and activities</p>
    </div>
    <div class="panel panel-form">
      <div class="field">Name</div>
      <div class="send">SEND</div>
    </div>
  </section>

  <footer class="footer">
    <div class="col" style="left:36px"><h4>CONTACT</h4><ul><li>tell: +61 2 5550 140 221</li><li>fax: +61 2 5550 140 222</li><li>Email: info@tidewell.com.au</li><li>www.tidewell.com.au</li></ul></div>
    <div class="divider" style="left:255px"></div>
    <div class="col" style="left:272px"><h4>SOCIAL MEDIA</h4><ul><li>tell: +61 2 5550 140 221</li><li>fax: +61 2 5550 140 222</li><li>Email: info@tidewell.com.au</li><li>www.tidewell.com.au</li></ul></div>
    <div class="divider" style="left:492px"></div>
    <div class="col" style="left:509px"><h4>BLOG</h4><ul><li>tell: +61 2 5550 140 221</li><li>fax: +61 2 5550 140 222</li><li>Email: info@tidewell.com.au</li><li>www.tidewell.com.au</li></ul></div>
    <div class="divider" style="left:728px"></div>
    <div class="col" style="left:746px"><h4>PARTNERS</h4><ul><li>tell: +61 2 5550 140 221</li><li>fax: +61 2 5550 140 222</li><li>Email: info@tidewell.com.au</li><li>www.tidewell.com.au</li></ul></div>
  </footer>
</div>
</body>
</html>
```